Velmora Roasters Business Needs a Wordpress Design

We need a Wordpress design for a Velmora Roasters E-commerce based in Sao Paulo, Brazil. We want something very similar to quennafield.com, but with a few exceptions, better described in the attachment (PLEASE READ our specifications). The product we're selling is premium, so we need to communicate sophistication, and at the same time people should feel they're in contact with an innovative company. Our company is called Velmora Roasters.
Target Market(s)
Adults aged 25 to 50 who have refined tastes.
Industry/Entity Type
Business
Colors
Designer to choose colors to be used in the design.
Look and feel

```html
<!DOCTYPE html>
<html lang="en">
<head>
<meta charset="utf-8">
<title>Velmora Roasters</title>
<link href="https://fonts.googleapis.com/css2?family=Kalam:wght@400&family=Noto+Sans:wght@400&display=swap" rel="stylesheet">
<style>
:root{
  --cream:#f2e7d4;
  --sand:#e4ddd1;
  --bar:#2a1a0c;
  --tab:#6b4527;
  --brown:#5f341a;
  --ink:#3c3a37;
  --footer:#141311;
  --white:#ffffff;
  --logo:#2c1d12;
}
*{margin:0;padding:0;box-sizing:border-box}
html,body{width:1154px;height:1200px;overflow:hidden;background:var(--sand)}
body{position:relative;font-family:Arial,Helvetica,sans-serif}
.abs{position:absolute}

.site-header{left:0;top:0;width:1154px;height:114px;background:var(--cream);border-top:4px solid var(--tab)}
.account-tab{left:614px;top:0;width:444px;height:34px;background:var(--tab);border-radius:0 0 4px 0;clip-path:polygon(0 0,100% 0,100% 100%,16px 100%);display:flex;justify-content:flex-end;align-items:center;padding-right:20px}
.account-tab a{flex-shrink:0;white-space:nowrap;color:var(--white);font-size:14px;text-decoration:none;margin-left:30px}
.brand{left:99px;top:40px;display:flex;align-items:center;gap:14px}
.brand-mark{width:18px;height:18px;border-radius:50%;background:var(--tab)}
.brand-name{font-family:"Noto Sans",sans-serif;font-size:34px;color:var(--logo)}

.main-nav{left:0;top:114px;width:1154px;height:49px;background:var(--bar)}
.main-nav a{position:absolute;top:0;line-height:49px;transform:translateX(-50%);color:var(--white);font-family:"Noto Sans",sans-serif;font-size:14px;text-decoration:none;white-space:nowrap}
.nav-sep{position:absolute;top:8px;width:1px;height:34px;background:#4a3524}

.hero{left:0;top:163px;width:1154px;height:496px;background:
  linear-gradient(100deg,rgba(0,0,0,0) 0%,rgba(0,0,0,0) 55%,rgba(235,228,220,.55) 80%,rgba(235,228,220,.35) 100%),
  linear-gradient(180deg,#3b200d 0%,#5e3d12 25%,#7a5220 50%,#8d5e35 75%,#9a6a45 100%)}
.hero-band{left:0;top:411px;width:820px;height:184px;background:linear-gradient(90deg,rgba(60,50,45,.55) 0%,rgba(60,50,45,.5) 80%,rgba(60,50,45,0) 100%)}
.hero-title{left:119px;top:414px;font-family:Kalam,cursive;font-size:50px;color:var(--white);line-height:1.2;font-weight:400;white-space:nowrap}
.hero-text{left:129px;top:478px;width:490px;font-size:13px;line-height:19.5px;color:var(--white)}
.hero-btn{left:135px;top:546px;width:127px;height:31px;background:var(--white);font-family:Kalam,cursive;font-size:21px;color:var(--brown);text-align:center;line-height:33px;letter-spacing:1px}

.feature{width:300px}
.feature-photo{position:absolute;left:0;top:0;width:300px;height:179px}
.feature-caption{position:absolute;left:0;top:99px;width:270px;height:39px;background:rgba(20,16,12,.65);font-family:Kalam,cursive;font-size:24px;color:var(--white);padding-left:15px;line-height:42px;white-space:nowrap}
.feature-text{position:absolute;left:0;top:205px;width:300px;font-size:13px;line-height:19.3px;color:var(--ink);text-align:justify}
.feature-btn{position:absolute;left:54px;top:319px;width:187px;height:44px;background:var(--brown);font-family:Kalam,cursive;font-size:21px;color:var(--white);text-align:center;line-height:47px;letter-spacing:1px}
.photo-warm{background:linear-gradient(180deg,#d58a2a 0%,#e8b36a 35%,#8a5a3a 70%,#5a3420 100%)}
.photo-roaster{background:linear-gradient(180deg,#ddd6b8 0%,#c9c0a0 45%,#3a3632 75%,#24201c 100%)}

.site-footer{left:0;top:1118px;width:1154px;height:82px;background:var(--footer)}
.footer-links{left:96px;top:18px;display:flex;color:var(--white);font-size:15px;white-space:nowrap}
.footer-links span{margin-right:26px}
.copyright{left:95px;top:50px;font-size:12.5px;color:var(--white);letter-spacing:.3px;white-space:nowrap}
.newsletter-input{left:737px;top:26px;width:227px;height:35px;background:var(--white);border-radius:4px}
.newsletter-btn{left:972px;top:26px;width:75px;height:34px;background:var(--brown);border:1px solid #cfc3b4;border-radius:4px;color:var(--white);font-size:14px;text-align:center;line-height:32px}
</style>
</head>
<body>

<header class="abs site-header">
  <nav class="abs account-tab">
    <a>My Account</a><a>My Wishlist</a><a>My Cart</a><a>Checkout</a><a>Log in</a>
  </nav>
  <div class="abs brand">
    <span class="brand-mark"></span>
    <span class="brand-name">Velmora Roasters</span>
  </div>
</header>

<nav class="abs main-nav">
  <a style="left:119px">Home</a>
  <span class="nav-sep" style="left:181px"></span>
  <a style="left:277px">Brewing Guides</a>
  <span class="nav-sep" style="left:371px"></span>
  <a style="left:459px">Subscriptions</a>
  <span class="nav-sep" style="left:544px"></span>
  <a style="left:631px">Merchandise</a>
  <span class="nav-sep" style="left:715px"></span>
  <a style="left:774px">Blog</a>
  <span class="nav-sep" style="left:834px"></span>
  <a style="left:908px">Our Story</a>
  <span class="nav-sep" style="left:983px"></span>
  <a style="left:1041px">Cart</a>
</nav>

<section class="abs hero" role="img" aria-label="Cup of coffee on a saucer with a spoon, falling sugar cubes and coffee beans on a wooden table"></section>
<div class="abs hero-band"></div>
<h1 class="abs hero-title">Coffee Of The Month</h1>
<p class="abs hero-text">Lorem Ipsum is that it has a more-or-less normal distribution of letters, as opposed to using 'Content here, content here', making it look like readable English. Many desktop publishing packages and web page</p>
<div class="abs hero-btn">MORE INFO</div>

<article class="abs feature" style="left:97px;top:716px">
  <div class="feature-photo photo-warm" role="img" aria-label="Coffee cup beside a sack of roasted beans"></div>
  <div class="feature-caption">Coffee plant</div>
  <p class="feature-text">Lorem Ipsum is that it has a more-or-less normal distribution of letters, as opposed to using 'Content here, content here', making it look like readable English. Many desktop publishing packages and web page.</p>
  <div class="feature-btn">MORE INFO</div>
</article>

<article class="abs feature" style="left:426px;top:716px">
  <div class="feature-photo photo-roaster" role="img" aria-label="Coffee roasting machine in a workshop"></div>
  <div class="feature-caption">Roasting machine</div>
  <p class="feature-text">Lorem Ipsum is that it has a more-or-less normal distribution of letters, as opposed to using 'Content here, content here', making it look like readable English. Many desktop publishing packages and web page.</p>
  <div class="feature-btn">MORE INFO</div>
</article>

<article class="abs feature" style="left:758px;top:716px">
  <div class="feature-photo photo-warm" role="img" aria-label="Coffee cup beside a sack of roasted beans"></div>
  <div class="feature-caption">Shipping process</div>
  <p class="feature-text">Lorem Ipsum is that it has a more-or-less normal distribution of letters, as opposed to using 'Content here, content here', making it look like readable English. Many desktop publishing packages and web page.</p>
  <div class="feature-btn">MORE INFO</div>
</article>

<footer class="abs site-footer">
  <div class="abs footer-links">
    <span>Contact</span><span>|</span>
    <span>Special</span><span>|</span>
    <span>Orders</span><span>|</span>
    <span>Wholesale</span><span>|</span>
    <span>Press</span><span>|</span>
    <span>Faq</span>
  </div>
  <p class="abs copyright">Shipping and Returns Terms of Use Privacy © 2013 Aldermoor Coffee Inc., All Rights Reserved</p>
  <div class="abs newsletter-input"></div>
  <div class="abs newsletter-btn">Sign up</div>
</footer>

</body>
</html>
```